MOSSGATE SPIRITWORKS WEBSITE

MOSSGATE SPIRITWORKS WHOLESALES ALCOHOL (WHISKY VODKA AND HELPS CREATES BOTTLING/BRANDING FOR PEOPLE WANTING LAUNCH THERE OWN BRANDS OF ALCOHOL

Colors

Designer to choose colors to be used in the design.

```html
<!DOCTYPE html>
<html lang="en">
<head>
<meta charset="utf-8">
<title>Mossgate Spiritworks</title>
<link href="https://fonts.googleapis.com/css2?family=Montserrat:wght@400;500;600;700;800&display=swap" rel="stylesheet">
<style>
:root{
  --dark:#2f2b27;
  --darker:#151312;
  --gold:#f0b323;
  --cream:#faebc9;
  --tan:#d4b68b;
  --light:#f3f3f2;
  --ink:#161616;
  --body:#333;
  --muted:#bcb5ab;
  --white:#fff;
}
*{margin:0;padding:0;box-sizing:border-box}
html,body{width:1200px;height:4387px;overflow:hidden}
body{font-family:'Montserrat',sans-serif;color:var(--ink);background:var(--white);position:relative}
.abs{position:absolute}
.ph{position:absolute;display:block}

/* header */
.site-header{position:absolute;left:0;top:0;width:1200px;height:111px;background:var(--dark)}
.brand{position:absolute;display:flex;align-items:center;gap:12px;color:var(--white);font-weight:600;letter-spacing:1px}
.brand-mark{width:16px;height:16px;background:var(--gold)}
.header-brand{left:94px;top:40px;font-size:22px}
.nav{position:absolute;top:46px;left:0;font-size:13px;font-weight:600;color:var(--white)}
.nav span{position:absolute;white-space:nowrap}

/* hero */
.hero{position:absolute;left:0;top:111px;width:1200px;height:701px;background:linear-gradient(100deg,#3a2a1c 0%,#6a4a2a 35%,#a87a40 60%,#c89a55 75%,#6b4a2c 100%)}
.hero-kicker{left:140px;top:312px;font-size:31px;font-weight:600;color:var(--gold)}
.hero-title{left:138px;top:345px;font-size:62px;font-weight:800;color:var(--white);white-space:nowrap}
.hero-text{left:145px;top:432px;width:460px;font-size:16px;font-weight:600;line-height:23px;color:var(--white)}
.btn{position:absolute;display:flex;align-items:center;justify-content:center;background:var(--gold);color:var(--ink);font-size:17px;font-weight:500;border-radius:4px}

/* shop cards */
.shop-card{position:absolute;top:877px;height:95px;background:var(--cream);border-radius:4px}
.shop-card .label{position:absolute;left:86px;top:18px;font-size:18px;color:#555}
.shop-card .name{position:absolute;left:86px;top:42px;font-size:28px;font-weight:500}
.bottle{position:absolute;top:846px;width:60px;height:142px;border-radius:8px 8px 4px 4px}

/* wholesale */
.watermark{left:0;top:1000px;width:1200px;text-align:center;font-size:140px;font-weight:800;letter-spacing:8px;color:#f1f1f1}
.kicker{font-size:37px;font-weight:600;color:var(--gold)}
.title{font-size:58px;font-weight:800;color:var(--ink);white-space:nowrap}
.center{left:0;width:1200px;text-align:center}
.lead{font-size:16px;line-height:23px;color:var(--body)}
.tile{position:absolute;width:303px;height:192px;border-radius:6px}
.tile-label{position:absolute;font-size:18px;color:#555}
.tile-name{position:absolute;font-size:28px;font-weight:500}
.partner{position:absolute;top:2100px;font-size:22px;font-weight:600;color:#8a8a8a;text-align:center;width:220px}
.dots{left:585px;top:2201px;display:flex;gap:6px}
.dots i{width:5px;height:5px;border-radius:50%;background:#d9d9d9;display:block}
.dots i:first-child{background:var(--gold)}

/* services */
.band{left:0;top:2267px;width:1200px;height:58px;background:var(--tan)}
.services{left:0;top:2325px;width:1200px;height:1096px;background:linear-gradient(160deg,#f6f6f5,#ececea 60%,#f5f5f4)}
.step-title{position:absolute;left:201px;top:2730px;font-size:24px;font-weight:700;color:var(--gold)}
.step-text{position:absolute;left:201px;top:2777px;width:370px;font-size:16px;line-height:23px;color:var(--body)}
.step-text u{color:#999}
.dot{position:absolute;width:26px;height:26px;border-radius:50%;border:3px solid var(--gold)}
.dot.active{background:var(--gold)}
.step-item{position:absolute;left:199px;font-size:25px;font-weight:700}
.timeline{left:154px;top:2760px;width:3px;height:236px;background:var(--gold)}

/* talk */
.talk{left:0;top:3421px;width:1200px;height:592px;background:linear-gradient(100deg,#0e0d0c,#211e1c 60%,#2b2826)}
.talk-text{left:485px;top:3644px;width:490px;font-size:16px;line-height:26.5px;color:#e8e8e8}

/* footer */
.site-footer{left:0;top:4013px;width:1200px;height:374px;background:var(--dark)}
.foot-head{position:absolute;top:4072px;font-size:17px;font-weight:600;color:var(--muted)}
.foot-list{position:absolute;top:4111px;list-style:none;font-size:14px;line-height:27px;color:var(--white)}
.foot-list .phone{color:var(--gold);text-decoration:underline}
.foot-rule{left:140px;top:4281px;width:920px;height:1px;background:#4a453f}
.footer-brand{left:145px;top:4326px;font-size:20px}
.copyright{left:374px;top:4332px;font-size:10px;color:var(--white)}
</style>
</head>
<body>

<header class="site-header">
  <div class="brand header-brand"><span class="brand-mark"></span>MOSSGATE SPIRITWORKS</div>
  <nav class="nav">
    <span style="left:491px">Home</span>
    <span style="left:583px">About</span>
    <span style="left:675px">Wholesale</span>
    <span style="left:796px">Services</span>
    <span style="left:903px">Contact</span>
  </nav>
</header>

<section class="hero" role="img" aria-label="Whisky being poured over ice with an orange peel garnish in a tumbler"></section>
<p class="abs hero-kicker">Turn your next drink idea</p>
<h1 class="abs hero-title">Into a Reality</h1>
<p class="abs hero-text">We have exclusive access to spirits from world-class distilleries globally producing award winning We are able to supply large volumes world-wide if you wish to bottle in your own facility.</p>
<a class="btn" style="left:141px;top:553px;width:393px;height:50px">CREATE YOUR BRAND</a>

<div class="shop-card" style="left:51px;width:344px"><span class="label">Shop</span><span class="name">Vodka</span></div>
<div class="shop-card" style="left:446px;width:328px"><span class="label">Shop</span><span class="name">Whisky</span></div>
<div class="shop-card" style="left:817px;width:339px"><span class="label">Create</span><span class="name">Your Branding</span></div>
<span class="bottle" style="left:46px;background:linear-gradient(#c76a12,#e39a2a)" role="img" aria-label="Bottle of amber spirit"></span>
<span class="bottle" style="left:442px;background:linear-gradient(#1a1a1a,#3a2a1a)" role="img" aria-label="Bottle of whisky"></span>
<span class="bottle" style="left:815px;background:linear-gradient(#5a1a12,#8a3a22)" role="img" aria-label="Bottle of cognac"></span>

<div class="abs watermark">MOSSGATE</div>
<p class="abs center kicker" style="top:1108px">Wholesale</p>
<h2 class="abs center title" style="top:1143px">World-class spirits</h2>
<p class="abs lead" style="left:270px;top:1233px;width:660px;text-align:center">We have exclusive access to spirits from world-class distilleries globally producing award winning We are able to supply large volumes of high-end spirit world-wide if you wish to bottle in your own facility.</p>

<span class="tile" style="left:70px;top:1355px;background:linear-gradient(120deg,#3a2418,#8a5a32,#2a1a12)" role="img" aria-label="Whisky decanter and glass"></span>
<span class="tile" style="left:448px;top:1355px;background:linear-gradient(120deg,#1a1f22,#6a767a,#c8ced0)" role="img" aria-label="Vodka splashing in shot glasses"></span>
<span class="tile" style="left:827px;top:1355px;background:linear-gradient(120deg,#4a5a52,#9a8a72,#c89a7a)" role="img" aria-label="Rum cocktails and bottle"></span>
<span class="tile" style="left:70px;top:1655px;background:linear-gradient(120deg,#c8b88a,#1a4a9a,#e8e4da)" role="img" aria-label="Gin bottles"></span>
<span class="tile" style="left:448px;top:1655px;background:linear-gradient(120deg,#8a7a62,#3a1a1a,#d8ccb8)" role="img" aria-label="Red wine bottle and glass"></span>
<span class="tile" style="left:827px;top:1655px;background:linear-gradient(180deg,#2a6a8a,#1a3a5a 60%,#d8d4cc)" role="img" aria-label="Champagne bottle by the sea"></span>

<span class="tile-label" style="left:104px;top:1561px">Shop</span><span class="tile-name" style="left:104px;top:1584px">Whiskies</span>
<span class="tile-label" style="left:488px;top:1561px">Shop</span><span class="tile-name" style="left:488px;top:1584px">Vodka</span>
<span class="tile-label" style="left:848px;top:1561px">Shop</span><span class="tile-name" style="left:848px;top:1584px">Rum</span>
<span class="tile-label" style="left:104px;top:1864px">Shop</span><span class="tile-name" style="left:104px;top:1887px">Gins</span>
<span class="tile-label" style="left:488px;top:1864px">Shop</span><span class="tile-name" style="left:488px;top:1887px">Wines</span>
<span class="tile-label" style="left:848px;top:1864px">Shop</span><span class="tile-name" style="left:848px;top:1887px">Champagnes</span>

<a class="btn" style="left:397px;top:1961px;width:391px;height:51px">ALL BRANDS</a>

<span class="partner" style="left:130px">Hollis Creek</span>
<span class="partner" style="left:361px">Ardmoor Reserve</span>
<span class="partner" style="left:578px">Calloway Finest</span>
<span class="partner" style="left:853px">Grey Heron Scotch</span>
<div class="abs dots"><i></i><i></i><i></i><i></i><i></i></div>

<div class="abs band"></div>
<section class="abs services"></section>
<p class="abs kicker" style="left:143px;top:2425px">Services</p>
<h2 class="abs title" style="left:141px;top:2460px">Create your brand</h2>
<p class="abs lead" style="left:143px;top:2549px;width:910px">Mossgate can bring your vision to life with our inhouse teams. We are here to help you through the entire process of creating unique spirit to compliment your brand. From formulating the recipe to production and even to helping you market your newest drink.</p>
<p class="abs lead" style="left:143px;top:2640px">We work directly with you to develop the perfect recipe and produce your drink</p>

<div class="abs timeline"></div>
<span class="dot active" style="left:142px;top:2731px"></span>
<h3 class="step-title">Recipe Development</h3>
<p class="step-text">With your drink recipe ready, it's time to start production. We begin by producing a test batch of your drink and let you make any final tweaks to the recipe and we invite you to see every step of the process of your drink being made. <u>learn more..</u></p>
<a class="btn" style="left:201px;top:2927px;width:393px;height:50px">CREATE NOW</a>

<span class="dot" style="left:142px;top:3008px"></span><span class="step-item" style="top:3005px">Trial Production</span>
<span class="dot" style="left:142px;top:3057px"></span><span class="step-item" style="top:3054px">Small Batch &amp; Spirit Bottling</span>
<span class="dot" style="left:142px;top:3108px"></span><span class="step-item" style="top:3105px">Canning Services</span>
<span class="dot" style="left:142px;top:3158px"></span><span class="step-item" style="top:3155px">Concept to Shelf</span>
<span class="dot" style="left:142px;top:3207px"></span><span class="step-item" style="top:3204px">Branding</span>

<div class="abs" style="left:854px;top:2676px;width:256px;height:252px;background:#c9c9c9;border-radius:4px"></div>
<span class="ph" style="left:749px;top:2723px;width:306px;height:528px;background:linear-gradient(150deg,#c8a860,#e8dcc0 40%,#1a1a1a 70%,#0a0a0a);border-radius:6px" role="img" aria-label="Champagne bottle and dark bottle neck"></span>
<span class="ph" style="left:631px;top:2863px;width:300px;height:408px;background:linear-gradient(180deg,#f2f2f2,#f0c8d0 55%,#e88ca0);border-radius:4px" role="img" aria-label="Rosé wine bottle on a white card"></span>

<section class="abs talk"></section>
<span class="ph" style="left:0;top:3421px;width:485px;height:592px;background:radial-gradient(ellipse at 50% 75%,#b0701a,#3a2410 45%,#0e0d0c 75%)" role="img" aria-label="Tasting glasses with whisky"></span>
<p class="abs kicker" style="left:485px;top:3512px">Let’s talk</p>
<h2 class="abs title" style="left:483px;top:3547px;color:var(--white)">Recipe Development</h2>
<p class="abs talk-text">Turn your next drink idea into a reality and share your product with the world.<br>Mossgate can bring your vision to life with our inhouse teams. We are here to help you through the entire process of creating unique spirit to compliment your brand. From formulating the recipe to production and even to helping you market your newest drink;</p>
<a class="btn" style="left:487px;top:3877px;width:393px;height:51px">CONTACT US</a>

<footer class="abs site-footer"></footer>
<h4 class="foot-head" style="left:140px">CREATE A NEW BRAND</h4>
<h4 class="foot-head" style="left:483px">CREATE A NEW BRAND</h4>
<h4 class="foot-head" style="left:815px">CREATE A NEW BRAND</h4>
<ul class="foot-list" style="left:143px"><li>Home</li><li>About</li><li>Wholesale</li><li>Services</li><li>Contact</li></ul>
<ul class="foot-list" style="left:482px"><li>Recipe Development</li><li>Trial Production</li><li>Small Batch &amp; Spirit Bottling</li><li>Canning Services</li><li>Concept to Shelf</li><li>Branding</li></ul>
<ul class="foot-list" style="left:836px"><li class="phone">+(31) 612 345 098</li><li>Mossgate Spiritworks Building 12,</li><li>Havenweg 48,</li><li>Noordwijk, 2201AB</li><li>Netherlands</li></ul>
<div class="abs foot-rule"></div>
<div class="brand footer-brand"><span class="brand-mark"></span>MOSSGATE SPIRITWORKS</div>
<p class="abs copyright">Copyright © 2022 Mossgate. Use of this website constitutes acceptance of our User Agreement and Privacy Policy.</p>

</body>
</html>
```